Need updated stationery design for chiropractic clinic

We recently moved our office and are looking to refresh our letterhead, business cards, presentation folder and envelopes. I tend to prefer simple, clean designs. We communicate with a lot of attorneys and want to exude professionalism. I have attached our logo and 2 additional versions (all white and white letters instead of grey).

Target Market(s)

Other medical professionals and attorneys. Business cards will go to patients as well.

Industry/Entity Type

Healthcare

```html
<!DOCTYPE html>
<html lang="en">
<head>
<meta charset="utf-8">
<title>Restora Stationery Set</title>
<link href="https://fonts.googleapis.com/css2?family=Source+Sans+3:wght@600&display=swap" rel="stylesheet">
<style>
  :root {
    --teal: #00cdd1;
    --teal-deep: #2aa5a6;
    --paper: #ffffff;
    --paper-shade: #f3f3f3;
    --rule: #7fe3e6;
    --backdrop: #aaaaaa;
    --crease: #00b9bd;
  }
  html, body {
    margin: 0;
    width: 1200px;
    height: 856px;
    overflow: hidden;
    background: var(--backdrop);
  }
  .canvas {
    position: relative;
    width: 1200px;
    height: 856px;
    font-family: "Source Sans 3", sans-serif;
  }
  .piece { position: absolute; box-sizing: border-box; }
  .brand-name {
    position: absolute;
    margin: 0;
    font-weight: 600;
    color: var(--teal);
    line-height: 1;
    white-space: nowrap;
  }
  .brand-name.on-teal { color: var(--paper); }
  .rule { position: absolute; height: 1px; background: var(--rule); }

  /* Letterheads */
  .letterhead {
    width: 228px; height: 323px;
    background: linear-gradient(160deg, var(--paper) 0%, var(--paper-shade) 55%, var(--paper) 100%);
  }
  .letterhead--classic { left: 96px; top: 84px; }
  .letterhead--banded { left: 96px; top: 437px; background: var(--paper); }
  .letterhead__band {
    position: absolute; left: 0; top: 0; width: 100%; height: 41px;
    background: var(--teal);
  }

  /* Folder */
  .folder-cover {
    left: 354px; top: 83px; width: 473px; height: 336px;
    background: var(--teal);
  }
  .folder-cover__spine {
    position: absolute; left: 227px; top: 0; width: 4px; height: 100%;
    background: var(--crease);
  }
  .folder-inside {
    left: 349px; top: 434px; width: 476px; height: 336px;
    background: var(--teal);
  }
  .folder-inside__pocket { position: absolute; left: 0; top: 0; }

  /* Envelopes */
  .envelope { width: 251px; background: var(--paper); }
  .envelope--window { left: 856px; top: 84px; height: 112px; border-top: 1px solid var(--rule); }
  .envelope__window {
    position: absolute; left: 24px; top: 56px; width: 84px; height: 37px;
    border-radius: 3px;
    background: linear-gradient(90deg, var(--teal), var(--teal-deep));
  }
  .envelope--open { left: 857px; top: 232px; height: 146px; background: transparent; }
  .envelope--closed { left: 856px; top: 416px; height: 110px; background: transparent; }
  .envelope svg { position: absolute; left: 0; top: 0; }

  /* Business cards */
  .card { left: 858px; width: 110px; height: 63px; }
  .card--front { top: 582px; background: var(--paper); }
  .card--back { top: 659px; background: var(--teal); }
</style>
</head>
<body>
<main class="canvas">

  <section class="piece letterhead letterhead--classic" aria-label="Letterhead">
    <p class="brand-name" style="left:25px; top:19px; font-size:10px;">Restora</p>
    <div class="rule" style="left:33px; top:41px; width:167px;"></div>
  </section>

  <section class="piece letterhead letterhead--banded" aria-label="Letterhead with header band">
    <div class="letterhead__band">
      <p class="brand-name on-teal" style="left:85px; top:15px; font-size:10px;">Restora</p>
    </div>
  </section>

  <section class="piece folder-cover" aria-label="Presentation folder cover">
    <div class="folder-cover__spine"></div>
    <p class="brand-name on-teal" style="left:297px; top:80px; font-size:20px;">Restora</p>
  </section>

  <section class="piece folder-inside" aria-label="Presentation folder inside">
    <svg class="folder-inside__pocket" width="476" height="336" viewBox="0 0 476 336">
      <rect x="240" y="0" width="236" height="336" fill="#00cdd1"/>
      <rect x="246" y="5" width="230" height="331" fill="#f7f7f7"/>
      <path d="M476 2 C455 5 446 12 432 30 L289 290 L255 290 Q241 290 241 304 L241 336 L476 336 Z"
            fill="#ffffff" stroke="#e2e2e2" stroke-width="1"/>
    </svg>
    <p class="brand-name" style="left:272px; top:23px; font-size:10px;">Restora</p>
    <div class="rule" style="left:279px; top:47px; width:137px;"></div>
    <p class="brand-name" style="left:391px; top:301px; font-size:10px;">Restora</p>
  </section>

  <section class="piece envelope envelope--window" aria-label="Window envelope front">
    <p class="brand-name" style="left:24px; top:22px; font-size:10px;">Restora</p>
    <div class="envelope__window"></div>
  </section>

  <section class="piece envelope envelope--open" aria-label="Envelope back, flap open">
    <svg width="251" height="146" viewBox="0 0 251 146">
      <rect x="0" y="40" width="251" height="106" fill="#fafafa"/>
      <path d="M0 40 L126 66 L251 40" fill="none" stroke="#e0e0e0" stroke-width="1"/>
      <path d="M0 40 L18 10 Q24 0 34 0 L217 0 Q227 0 233 10 L251 40 Z" fill="#00cdd1"/>
    </svg>
    <p class="brand-name" style="left:57px; top:45px; font-size:9px;">Restora</p>
  </section>

  <section class="piece envelope envelope--closed" aria-label="Envelope back, flap closed">
    <svg width="251" height="110" viewBox="0 0 251 110">
      <rect x="0" y="0" width="251" height="110" fill="#fafafa"/>
      <path d="M0 0 L251 0 L233 28 Q226 40 214 40 L37 40 Q25 40 18 28 Z" fill="#00cdd1"/>
    </svg>
  </section>

  <section class="piece card card--front" aria-label="Business card front">
    <p class="brand-name" style="left:9px; top:7px; font-size:5px;">Restora</p>
    <div class="rule" style="left:11px; top:15px; width:84px;"></div>
  </section>

  <section class="piece card card--back" aria-label="Business card back">
    <p class="brand-name on-teal" style="left:31px; top:26px; font-size:10px;">Restora</p>
  </section>

</main>
</body>
</html>
```